Bourbon Label Design For a Unique Craft Distillery

We are a craft distillery located in Mount Holly Nj looking for a label design for our new bourbon brand. The Name of the bourbon is going to be called "Iron Meadow" and the type of bourbon is a "straight Bourbon Whiskey". The First file are the pictures of our current brands. Would like the design to look Vintage but pop. The Bourbon will be a top shelf item. The Pictures of the other bottle are brands we like.

Target Market(s)

21-65 years old

Font styles to use
Decorative
Script

Colors
ec1f27
3176b5
1b1b1b
f5f5f5

Requirements
Must have
• vintage look, and pop !

```html
<!DOCTYPE html>
<html lang="en">
<head>
<meta charset="utf-8">
<title>Iron Meadow Straight Bourbon Whiskey – Label</title>
<link href="https://fonts.googleapis.com/css2?family=Oswald:wght@500;600&family=Pinyon+Script&family=Courier+Prime:wght@700&display=swap" rel="stylesheet">
<style>
  :root {
    --backdrop: #ffffff;
    --paper: #f5f4f1;
    --paper-edge: #e9e7e2;
    --label-red: #b3222b;
    --foil-gold: #c9a24c;
    --ink: #1b1b1b;
    --engraving-light: #d6d6d6;
    --engraving-dark: #3a3a3a;
  }
  * { box-sizing: border-box; margin: 0; padding: 0; }
  html, body {
    width: 1200px; height: 900px; overflow: hidden;
    background: var(--backdrop);
  }
  .canvas { position: relative; width: 1200px; height: 900px; }

  .label {
    position: absolute; left: 330px; top: 72px;
    width: 540px; height: 756px;
    background: radial-gradient(ellipse at center, var(--paper) 60%, var(--paper-edge) 100%);
    box-shadow: 0 1px 4px rgba(0,0,0,.12);
    color: var(--label-red);
    text-align: center;
  }
  .label > * { position: absolute; }

  .frame-lines { left: 0; top: 0; width: 540px; height: 756px; }

  .locomotive-art {
    left: 112px; top: 30px; width: 306px; height: 186px;
    background: linear-gradient(180deg, var(--engraving-light) 0%, var(--engraving-dark) 65%, #8a8a8a 100%);
    border-radius: 4px;
  }

  .brand-name {
    left: 0; right: 0; top: 214px;
    font-family: "Oswald", sans-serif; font-weight: 600;
    font-size: 82px; line-height: 1; letter-spacing: 0;
    text-transform: uppercase; white-space: nowrap;
  }

  .divider { left: 60px; width: 420px; height: 30px; border-radius: 15px; }
  .divider--red { top: 328px; background: linear-gradient(90deg, transparent, var(--label-red) 20%, var(--label-red) 80%, transparent); opacity: .55; }
  .divider--gold { top: 578px; background: linear-gradient(90deg, transparent, var(--foil-gold) 20%, var(--foil-gold) 80%, transparent); opacity: .6; }

  .spirit-type {
    left: 0; right: 0; top: 384px;
    font-family: "Oswald", sans-serif; font-weight: 500;
    font-size: 38px; line-height: 1; letter-spacing: 1px;
    text-transform: uppercase; white-space: nowrap;
  }

  .origin-script {
    left: 0; right: 0; top: 440px;
    font-family: "Pinyon Script", cursive;
    font-size: 46px; line-height: 1.1;
    color: var(--foil-gold); white-space: nowrap;
  }

  .origin-in {
    left: 0; right: 0; top: 510px;
    font-family: "Courier Prime", monospace; font-weight: 700;
    font-size: 12px; letter-spacing: 2px;
  }

  .origin-place {
    left: 0; right: 0; top: 532px;
    font-family: "Courier Prime", monospace; font-weight: 700;
    font-size: 22px; letter-spacing: 5px; white-space: nowrap;
  }

  .stat { top: 644px; width: 150px; line-height: 1; }
  .stat--abv { left: 24px; }
  .stat--volume { right: 24px; }
  .stat-value {
    display: block;
    font-family: "Oswald", sans-serif; font-weight: 500; font-size: 36px;
  }
  .stat-caption {
    display: block; margin-top: 2px;
    font-family: "Pinyon Script", cursive; font-size: 26px; color: var(--ink);
  }

  .batch {
    left: 170px; width: 200px; top: 696px;
    font-family: "Courier Prime", monospace; font-weight: 700;
    font-size: 14px; letter-spacing: 3px;
  }
</style>
</head>
<body>
<main class="canvas">
  <section class="label" aria-label="Iron Meadow bourbon label">
    <svg class="frame-lines" viewBox="0 0 540 756" aria-hidden="true">
      <g stroke="var(--foil-gold)" stroke-width="2" fill="none">
        <line x1="20" y1="40" x2="520" y2="40"/>
        <line x1="30" y1="24" x2="30" y2="110"/>
        <line x1="510" y1="24" x2="510" y2="110"/>
      </g>
      <g stroke="var(--label-red)" stroke-width="2">
        <line x1="175" y1="638" x2="365" y2="638"/>
        <line x1="175" y1="646" x2="365" y2="646"/>
        <line x1="175" y1="702" x2="215" y2="702"/>
        <line x1="175" y1="708" x2="215" y2="708"/>
        <line x1="325" y1="702" x2="365" y2="702"/>
        <line x1="325" y1="708" x2="365" y2="708"/>
      </g>
    </svg>

    <div class="locomotive-art" role="img" aria-label="Engraved illustration of a vintage steam locomotive"></div>

    <h1 class="brand-name">Iron Meadow</h1>

    <div class="divider divider--red" role="img" aria-label="Red filigree scroll ornament"></div>

    <p class="spirit-type">Straight Bourbon Whiskey</p>
    <p class="origin-script">Distilled Bottled &amp; Aged</p>
    <p class="origin-in">IN</p>
    <p class="origin-place">Alder Creek • KY</p>

    <div class="divider divider--gold" role="img" aria-label="Gold filigree scroll ornament"></div>

    <p class="stat stat--abv">
      <span class="stat-value">40%</span>
      <span class="stat-caption">Alc. by Vol.</span>
    </p>
    <p class="batch">BATCH#</p>
    <p class="stat stat--volume">
      <span class="stat-value">.75mL</span>
      <span class="stat-caption">Net. Wt.</span>
    </p>
  </section>
</main>
</body>
</html>
```